Corporate Brightfen business cards to be handed to investor, bankers etc. Needs to have a young feel

I need business cards designed for a technology company that provides uber-like rapid response on the security industry. I would like it simple but very cool and tasteful. See attached documents for artwork and colours to be used. Cut sheet describes business model. Card stock should be thicker than normal. I would like the one side to be just the art and the other to have the contact info with maybe the pin somewhere.

Target Market(s)

Investors

Industry/Entity Type

Business

Contact Information for Business Card

Would like the logo attached on one side with name address and other info on the other side.

Font styles to use
Other font styles liked:
• See existing logo

Colors
6b449b
886aae
e4daeb
ffffff

Requirements
Must have
• Name: Dorian Felkatsis
• Address: 47 Larkfield Avenue, Toronto, On, M6K2B7
• Tel: 416-7291846
• Email: rolo@brightfen.io
Nice to have
• See logo colours

```html
<!DOCTYPE html>
<html lang="en">
<head>
<meta charset="utf-8">
<title>Brightfen business cards</title>
<link rel="stylesheet" href="https://fonts.googleapis.com/css2?family=Work+Sans:wght@300;400&display=swap">
<style>
  :root {
    --bg: #1c1c1c;
    --card: #1e1e1e;
    --card-edge: #2a2a2a;
    --purple: #6b449b;
    --lilac: #886aae;
    --white: #ffffff;
    --text: #e8e8e8;
  }
  * { margin: 0; padding: 0; box-sizing: border-box; }
  html, body {
    width: 1200px; height: 897px; overflow: hidden;
    background: var(--bg);
    font-family: "Work Sans", Arial, sans-serif;
  }
  .card {
    position: absolute;
    left: 348px; width: 492px; height: 280px;
    background: linear-gradient(90deg, var(--card) 0%, #222 60%, var(--card-edge) 100%);
    box-shadow: 0 10px 24px rgba(0,0,0,.55);
    overflow: hidden;
  }
  .card--front { top: 158px; }
  .card--back { top: 468px; height: 278px; }
  .brand {
    position: absolute; display: flex; align-items: center;
    color: var(--white); font-weight: 300; letter-spacing: -0.5px;
  }
  .brand__dot {
    border-radius: 50%; background: var(--lilac); flex: none;
  }
  .card--front .brand { left: 26px; top: 122px; font-size: 32px; }
  .card--front .brand__dot { width: 14px; height: 14px; margin-right: 6px; margin-top: 6px; }
  .card--back .brand { left: 28px; top: 22px; font-size: 40px; }
  .card--back .brand__dot { width: 18px; height: 18px; margin-right: 7px; margin-top: 8px; }
  .feature-art {
    position: absolute; left: 284px; top: 66px; width: 204px; height: 210px;
    border-radius: 10px;
    background: linear-gradient(90deg, #1a1a1a 0%, #6e6e6e 55%, #e6e6e6 100%);
  }
  .card--back .feature-art { top: 66px; }
  .person { position: absolute; left: 29px; top: 102px; }
  .person__name { color: var(--lilac); font-size: 14.5px; font-weight: 400; letter-spacing: .3px; }
  .person__role { color: var(--text); font-size: 10.5px; margin-top: 2px; }
  .address {
    position: absolute; left: 27px; top: 166px;
    color: var(--text); font-size: 11.5px; line-height: 14px; letter-spacing: .6px; font-style: normal;
  }
  .contacts { position: absolute; left: 30px; top: 203px; list-style: none; }
  .contacts li {
    display: flex; align-items: center; height: 15.5px;
    color: var(--text); font-size: 11.5px; letter-spacing: .6px;
  }
  .contacts svg { width: 9px; height: 9px; margin-right: 9px; fill: none; stroke: var(--lilac); stroke-width: 1.4; }
</style>
</head>
<body>
  <section class="card card--front">
    <div class="brand"><span class="brand__dot"></span>brightfen</div>
    <div class="feature-art" role="img" aria-label="Large soft grey gradient brand artwork"></div>
  </section>

  <section class="card card--back">
    <div class="brand"><span class="brand__dot"></span>brightfen</div>
    <div class="person">
      <p class="person__name">Dorian Felkatsis</p>
      <p class="person__role">President</p>
    </div>
    <address class="address">47 Larkfield Avenue,<br>Toronto, On, M6K2B7</address>
    <ul class="contacts">
      <li><svg viewBox="0 0 10 10"><rect x="2.5" y="0.8" width="5" height="8.4" rx="0.8"/></svg>416-7291846</li>
      <li><svg viewBox="0 0 10 10"><rect x="0.8" y="2" width="8.4" height="6" /><path d="M0.8 2 5 5.5 9.2 2"/></svg>rolo@brightfen.io</li>
      <li><svg viewBox="0 0 10 10"><circle cx="5" cy="5" r="4"/><path d="M1 5h8M5 1c2 2 2 6 0 8M5 1c-2 2-2 6 0 8"/></svg>www.brightfen.io</li>
    </ul>
    <div class="feature-art" role="img" aria-label="Large soft grey gradient brand artwork"></div>
  </section>
</body>
</html>
```